Patent Law

Need to develop a home page for a patent lawyer.

Colors should go with logo, blues...

Company Name- Corvel Tindry, PLLC

Company Overview-

I am an Intellectual Property Lawyer and focus on patents, copyrights, trademarks, & trade secrets. I work with small businesses and start ups in the chemical and biotech industries.

Why Us-

I am small firm that can provide large-firm service at a reasonable price. I also can charge flat-fees for entreprenuers in certain practice areas.

Services-
Intellectual Property
Patents
Copyrights
Trademarks
Trade secrets
Healthcare Compliance
Elder law
Wills
Trusts

Website we like-
http://www.quarnlowtide.example/ - within industry!!
http://www.vopperhask.example/
http://dulbrickovan.example/
http://thefernwoldguides.example/

Target Market(s)

My customers will be small business, specifically small start-up companies in the chemical and biotech arena.

Industry/Entity Type

Trade

Requirements
Must have
• Colors should go with logo, blues...

```html
<!DOCTYPE html>
<html lang="en">
<head>
<meta charset="utf-8">
<title>Corvel Tindry, PLLC — Intellectual Property Law</title>
<link rel="stylesheet" href="https://fonts.googleapis.com/css2?family=Roboto:ital,wght@0,300;0,400;0,700;1,300;1,400;1,700&display=swap">
<style>
:root{
  --bar:#202020;
  --page:#e9e9e9;
  --panel:#ffffff;
  --blue:#1a8fd6;
  --button:#0d8ddb;
  --green:#4fc81a;
  --text:#3a3a3a;
  --muted:#555555;
  --line:#e4e4e4;
  --brand:#3b4250;
  --footer-text:#e6e6e6;
}
*{margin:0;padding:0;box-sizing:border-box}
html,body{width:1200px;height:1000px;overflow:hidden}
body{position:relative;background:var(--page);font-family:"Roboto",Arial,sans-serif;font-weight:300;color:var(--text)}
.abs{position:absolute}

.top-bar{left:0;top:0;width:1200px;height:42px;background:var(--bar)}
.social{top:8px;width:26px;height:26px;border-radius:3px}
.social--one{left:396px;background:#3fa9dd}
.social--two{left:430px;background:#3d5e9e}
.top-contact{right:185px;top:9px;color:#fff;font-size:17px;font-weight:300;white-space:nowrap}

.brand{left:185px;top:10px;width:190px;height:118px}
.brand-mark{position:absolute;left:50px;top:0;width:72px;height:72px;border-radius:50%;background:var(--blue)}
.brand-name{position:absolute;left:0;top:95px;font-size:18px;font-weight:400;color:var(--brand);letter-spacing:.3px;white-space:nowrap}

.main-nav{right:183px;top:103px;display:flex;gap:16px;font-size:18px;font-weight:300;color:var(--blue);white-space:nowrap}
.main-nav a{color:inherit;text-decoration:none}

.content-panel{left:182px;top:132px;width:838px;height:626px;background:var(--panel);box-shadow:0 0 3px rgba(0,0,0,.08)}

.hero{left:228px;top:167px;width:747px;height:206px;background:linear-gradient(100deg,#1a1a1a 0%,#3a3a3a 35%,#b9b9b9 55%,#6f6f6f 75%,#d4d4d4 100%);box-shadow:0 6px 8px -4px rgba(0,0,0,.25)}
.hero-caption{left:228px;top:178px;width:404px;height:104px;background:rgba(205,205,205,.88)}
.hero-text{left:243px;top:184px;width:380px;font-size:11px;line-height:20px;text-transform:uppercase;color:#333;font-weight:300;white-space:nowrap}

.btn{display:flex;align-items:center;justify-content:center;height:25px;background:var(--button);color:#fff;font-size:12px;font-weight:400;text-transform:uppercase;text-decoration:none;white-space:nowrap}
.hero-btn{left:525px;top:249px;width:99px}

.card{top:418px;width:266px;height:306px;border:1px solid var(--line);background:#fff}
.card--why{left:190px}
.card--services{left:468px}
.card--contact{left:746px}
.card-title{position:absolute;left:12px;top:6px;font-size:23px;font-style:italic;font-weight:300;color:var(--blue);white-space:nowrap}
.card--services .card-title{left:16px}
.card--contact .card-title{left:15px}
.card-rule{position:absolute;left:13px;top:37px;width:209px;height:1px;background:var(--blue)}
.card--services .card-rule{left:17px}
.card--contact .card-rule{left:18px}
.card .btn{position:absolute;right:8px;bottom:6px;width:100px}

.why-text{position:absolute;left:10px;top:60px;width:255px;font-size:12.5px;line-height:25px;text-transform:uppercase;color:var(--text);white-space:nowrap}
.why-text strong{font-weight:700;font-style:italic;color:#111}
.why-text .gap{height:50px}
.why-text .underline{border-bottom:1px solid #111}

.service-list{position:absolute;left:26px;top:59px;list-style:none}
.service-list li{display:flex;align-items:center;height:25.2px;font-size:13px;font-style:italic;text-transform:uppercase;color:var(--muted);white-space:nowrap}
.service-list svg{width:26px;height:20px;margin-right:6px}

.pin{position:absolute;left:65px;top:85px;width:124px;height:124px}

.site-footer{left:0;top:758px;width:1200px;height:212px;background:var(--bar)}
.footer-col{top:28px;color:var(--footer-text);font-size:14px;font-weight:300}
.footer-col h3{font-size:14px;font-weight:300;height:26px}
.footer-col li{list-style:none;height:25px}
.footer-col--one{left:266px}
.footer-col--two{left:558px}
.footer-col--three{left:843px}

.copyright{left:0;top:970px;width:1200px;height:30px;text-align:center;line-height:34px;font-size:12px;color:#333}
</style>
</head>
<body>

<header>
  <div class="abs top-bar"></div>
  <span class="abs social social--one" aria-label="Social profile"></span>
  <span class="abs social social--two" aria-label="Social profile"></span>
  <div class="abs top-contact">555-014-200 / MAP</div>

  <div class="abs brand">
    <span class="brand-mark"></span>
    <span class="brand-name">CORVEL TINDRY, PLLC</span>
  </div>

  <nav class="abs main-nav">
    <a href="#">HOME</a><span>-</span>
    <a href="#">ABOUT US</a><span>&nbsp;&nbsp;-</span>
    <a href="#">SERVICES</a><span>&nbsp;&nbsp;-</span>
    <a href="#">CONTACT US</a>
  </nav>
</header>

<main>
  <div class="abs content-panel"></div>

  <div class="abs hero" role="img" aria-label="Black and white photo of two people in business shirts shaking hands"></div>
  <div class="abs hero-caption"></div>
  <p class="abs hero-text">I am an intellectual property lawyer and focus on patents,<br>copyrights, trademarks, &amp; trade secrets. I work with small<br>businesses and start ups in the chemical and biotech industries</p>
  <a class="abs btn hero-btn" href="#">Find out more</a>

  <section class="abs card card--why">
    <h2 class="card-title">WHY US?</h2>
    <span class="card-rule"></span>
    <div class="why-text">
      <p>We are a small firm that can provide<br>a <strong>large-firm service</strong> at a <strong>great</strong><br>price. We believe in providing an<br>excellent service, all the time.</p>
      <div class="gap"></div>
      <p>Are you an <strong>entrepreneur?</strong> You<br>could <strong class="underline">pay less.</strong></p>
    </div>
    <a class="btn" href="#">Find out more</a>
  </section>

  <section class="abs card card--services">
    <h2 class="card-title">SERVICES</h2>
    <span class="card-rule"></span>
    <ul class="service-list">
      <li><svg viewBox="0 0 26 20"><path d="M2 11 L9 17 L24 3" fill="none" stroke="#4fc81a" stroke-width="4" stroke-linecap="round" stroke-linejoin="round"/></svg>Intellectual property</li>
      <li><svg viewBox="0 0 26 20"><path d="M2 11 L9 17 L24 3" fill="none" stroke="#4fc81a" stroke-width="4" stroke-linecap="round" stroke-linejoin="round"/></svg>Healthcare compliance</li>
      <li><svg viewBox="0 0 26 20"><path d="M2 11 L9 17 L24 3" fill="none" stroke="#4fc81a" stroke-width="4" stroke-linecap="round" stroke-linejoin="round"/></svg>Copyrights</li>
      <li><svg viewBox="0 0 26 20"><path d="M2 11 L9 17 L24 3" fill="none" stroke="#4fc81a" stroke-width="4" stroke-linecap="round" stroke-linejoin="round"/></svg>Trademarks</li>
      <li><svg viewBox="0 0 26 20"><path d="M2 11 L9 17 L24 3" fill="none" stroke="#4fc81a" stroke-width="4" stroke-linecap="round" stroke-linejoin="round"/></svg>Trade secrets</li>
      <li><svg viewBox="0 0 26 20"><path d="M2 11 L9 17 L24 3" fill="none" stroke="#4fc81a" stroke-width="4" stroke-linecap="round" stroke-linejoin="round"/></svg>Elder law</li>
      <li><svg viewBox="0 0 26 20"><path d="M2 11 L9 17 L24 3" fill="none" stroke="#4fc81a" stroke-width="4" stroke-linecap="round" stroke-linejoin="round"/></svg>Patents</li>
      <li><svg viewBox="0 0 26 20"><path d="M2 11 L9 17 L24 3" fill="none" stroke="#4fc81a" stroke-width="4" stroke-linecap="round" stroke-linejoin="round"/></svg>Wills</li>
      <li><svg viewBox="0 0 26 20"><path d="M2 11 L9 17 L24 3" fill="none" stroke="#4fc81a" stroke-width="4" stroke-linecap="round" stroke-linejoin="round"/></svg>Trusts</li>
    </ul>
    <a class="btn" href="#">Find out more</a>
  </section>

  <section class="abs card card--contact">
    <h2 class="card-title">CONTACT US</h2>
    <span class="card-rule"></span>
    <svg class="pin" viewBox="0 0 124 124" aria-label="Location">
      <circle cx="62" cy="62" r="62" fill="#0d8ddb"/>
      <path d="M62 104 C50 88 30 70 30 52 A32 32 0 0 1 94 52 C94 70 74 88 62 104 Z" fill="#fff"/>
      <circle cx="62" cy="53" r="15" fill="#0d8ddb"/>
    </svg>
    <a class="btn" href="#">Get in touch</a>
  </section>
</main>

<footer>
  <div class="abs site-footer">
    <div class="abs footer-col footer-col--one">
      <h3>QUICK LINKS</h3>
      <ul><li>NAV ITEM</li><li>NAV ITEM</li><li>NAV ITEM</li><li>NAV ITEM</li></ul>
    </div>
    <div class="abs footer-col footer-col--two">
      <h3>QUICK LINKS</h3>
      <ul><li>NAV ITEM</li><li>NAV ITEM</li><li>NAV ITEM</li><li>NAV ITEM</li></ul>
    </div>
    <div class="abs footer-col footer-col--three">
      <h3>QUICK LINKS</h3>
      <ul><li>NAV ITEM</li><li>NAV ITEM</li><li>NAV ITEM</li><li>NAV ITEM</li></ul>
    </div>
  </div>
  <div class="abs copyright">COPYRIGHT 2014 CORVEL TINDRY, PLLC</div>
</footer>

</body>
</html>
```